New Infographic-y Sales Diagram

We've got an asset affectionately known as "The Lantern," that needs a major update. First, we need a new logo applied. Second, we need the entire former design scrapped in favor of something better. Literally nothing should remain the same.

If you approximate the files given as a reference that would be enough. If, however, you can achieve something even better that we hadn't considered--that would truly be wonderful.

Target Market(s)

Homeowners. Preferably ones looking to make updates to their home. We do functional home renovations for folks.

Industry/Entity Type

Home Improvement

Font styles to use
Sans Serif

Colors

Designer to choose colors to be used in the design.

Requirements
Must have
• Some illustration work and and a generally unified theme.
Should not have
• Clip art or stock assets (excluding photography and icons if the icons are excellent).

```html
<!DOCTYPE html>
<html lang="en">
<head>
<meta charset="UTF-8">
<title>Hearth – Home Energy Upgrade Paths</title>
<link rel="stylesheet" href="https://fonts.googleapis.com/css2?family=Oswald:wght@400;500;600&display=swap">
<style>
  :root {
    --teal: #3391a6;
    --orange: #f39323;
    --orange-dark: #c46d12;
    --white: #ffffff;
    --frame: #000000;
  }
  * { margin: 0; padding: 0; box-sizing: border-box; }
  html, body { width: 1200px; height: 1200px; overflow: hidden; background: var(--white); }
  .canvas {
    position: relative;
    width: 1200px; height: 1200px;
    background: var(--white);
    border: 8px solid var(--frame);
    font-family: "Oswald", sans-serif;
    overflow: hidden;
  }
  .brand {
    position: absolute; left: 152px; top: 150px;
    display: flex; align-items: center; gap: 20px;
  }
  .brand-square { width: 52px; height: 52px; background: var(--orange); }
  .brand-name {
    font-weight: 600; font-size: 98px; line-height: 1;
    color: var(--teal); letter-spacing: 1px;
  }
  .house-illustration {
    position: absolute; left: 150px; top: 276px;
    width: 880px; height: 290px;
    background: linear-gradient(180deg, #3391a6 0%, #5aa9ba 70%, #f5b36a 100%);
  }
  .path-card {
    position: absolute;
    background: var(--teal);
    color: var(--white);
    overflow: visible;
  }
  .card-control { left: 152px; top: 653px; width: 255px; height: 377px; }
  .card-conserve { left: 454px; top: 641px; width: 271px; height: 401px; }
  .card-create { left: 771px; top: 653px; width: 255px; height: 377px; }
  .card-title-band {
    position: absolute; left: 0; right: 0; top: 69px; height: 48px;
    background: var(--white);
    display: flex; align-items: center; justify-content: center;
  }
  .card-title {
    font-weight: 500; font-size: 36px; color: var(--teal);
    letter-spacing: 0.5px; line-height: 1;
  }
  .card-body {
    position: absolute; left: 0; right: 0; top: 121px;
    padding: 0 8px;
  }
  .card-desc {
    text-align: center; text-transform: uppercase;
    font-size: 16px; line-height: 23.5px; letter-spacing: -0.2px;
  }
  .card-list {
    list-style: none; margin-top: 20px; padding-left: 16px;
    text-transform: uppercase; font-size: 18px; line-height: 26.4px;
  }
  .card-list li::before { content: "- "; }
  .ribbon {
    position: absolute; left: 0; top: 0;
    width: 290px; height: 160px;
    overflow: visible; pointer-events: none;
  }
  .ribbon-band { fill: var(--orange); }
  .ribbon-fold { fill: var(--orange-dark); }
  .ribbon-text {
    fill: var(--white); font-family: "Oswald", sans-serif;
    font-size: 16px; font-weight: 500; text-transform: uppercase;
  }
</style>
</head>
<body>
<main class="canvas">
  <header class="brand">
    <span class="brand-square"></span>
    <span class="brand-name">HEARTH</span>
  </header>

  <div class="house-illustration" role="img" aria-label="Flat illustration of a two-storey family house with garage, teal roofs and warm orange lit windows standing on a ground line"></div>

  <section class="path-card card-control">
    <div class="card-title-band"><h2 class="card-title">CONTROL</h2></div>
    <div class="card-body">
      <p class="card-desc">High comfort, low cost upgrades<br>that change the way you use energy.</p>
      <ul class="card-list">
        <li>HVAC</li><li>LED Lighting</li><li>Smart Thermostat</li><li>Smart Sensors</li>
      </ul>
    </div>
    <svg class="ribbon" viewBox="0 0 290 160" aria-hidden="true">
      <polygon class="ribbon-fold" points="255,91 262,91 262,99"/>
      <polygon class="ribbon-band" points="120,0 168,0 262,91 262,135"/>
      <text class="ribbon-text" text-anchor="middle" transform="translate(193,62) rotate(44)">Most Affordable</text>
    </svg>
  </section>

  <section class="path-card card-conserve">
    <div class="card-title-band" style="top:70px"><h2 class="card-title">CONSERVE</h2></div>
    <div class="card-body" style="top:120px">
      <p class="card-desc">Simple additions that cut out energy<br>waste without cutting in to your life.</p>
      <ul class="card-list">
        <li>Patio Covers</li><li>Water Heater</li><li>Insulation</li><li>Windows</li><li>Roofing</li>
      </ul>
    </div>
    <svg class="ribbon" viewBox="0 0 290 160" style="top:-7px" aria-hidden="true">
      <polygon class="ribbon-fold" points="271,90 279,90 279,98"/>
      <polygon class="ribbon-band" points="137,0 186,0 279,90 279,142"/>
      <text class="ribbon-text" text-anchor="middle" transform="translate(210,65) rotate(44)">Most Popular</text>
    </svg>
  </section>

  <section class="path-card card-create">
    <div class="card-title-band"><h2 class="card-title">CREATE</h2></div>
    <div class="card-body">
      <p class="card-desc">Big changes for the biggest savings.<br>Generate you own power<br>and kill your bill.</p>
      <ul class="card-list">
        <li>Solar</li><li>EV Chargers</li><li>Energy Storage</li>
      </ul>
    </div>
    <svg class="ribbon" viewBox="0 0 290 160" style="top:-6px" aria-hidden="true">
      <polygon class="ribbon-fold" points="255,97 262,97 262,105"/>
      <polygon class="ribbon-band" points="120,0 168,0 262,97 262,141"/>
      <text class="ribbon-text" text-anchor="middle" transform="translate(193,66) rotate(45)">Most Value</text>
    </svg>
  </section>
</main>
</body>
</html>
```